Website for an electrical contractor :)

We are after a web site which can show pictures of our jobs and our capability in a professional, creative and easily understood way.

----- Brightmoor Electrical ------

We really want a visually good looking website with three sections

Section one:
'Completed projects'
We have a few pictures of jobs which we've completed and would like to show off with a brief description. (see uploads)

Section two:
'Our capabilities'
Just a list of what services we offer

Section three:
We would like a 'contact us' section which people can send us a short msg and upload a file for plans to be able to send to us. We would need their name, phone number and email details. We would also need a short privacy policy saying 'we do not disclose information to third parties'.
We also want to display our contact number and postal address

Good luck :)

Target Market(s)

Adults 25 years+
Business owners
Builders
Real estate agents

Industry/Entity Type

Electrical

Colors

Designer to choose colors to be used in the design.

Requirements
Must have
• Visually appealing
Easy to understand
In the 'Completed projects' section, must have a list for each project we do i can upload pictures for it.

```html
<!DOCTYPE html>
<html lang="en">
<head>
<meta charset="utf-8">
<title>Brightmoor Electrical</title>
<link href="https://fonts.googleapis.com/css2?family=Open+Sans:wght@300;400;600&display=swap" rel="stylesheet">
<style>
:root{
  --red:#e0232a;
  --ink:#333333;
  --muted:#555555;
  --line:#d9d9d9;
  --band:#e6e6e6;
  --white:#ffffff;
  --hero-dark:#1c1a18;
}
*{box-sizing:border-box;margin:0;padding:0}
html,body{width:691px;height:1200px;overflow:hidden}
body{position:relative;background:var(--white);font-family:"Open Sans",Arial,sans-serif;color:var(--ink)}

.site-header{position:absolute;left:0;top:0;width:691px;height:62px}
.brand{position:absolute;left:46px;top:14px;display:flex;align-items:center;gap:8px;font-size:28px;font-weight:300;color:var(--ink);letter-spacing:-.5px}
.brand-dot{width:14px;height:14px;border-radius:50%;background:var(--red)}
.main-nav{position:absolute;top:26px;left:0;width:691px;font-size:10px}
.main-nav a{position:absolute;color:var(--ink);text-decoration:none}

.hero{position:absolute;left:0;top:62px;width:691px;height:272px;
  background:radial-gradient(circle at 34% 45%,#d9a15e 0,#7a5231 12%,transparent 30%),
             radial-gradient(circle at 80% 90%,#b6652a 0,transparent 22%),
             linear-gradient(90deg,#4a3a2c,var(--hero-dark) 60%,#3a2e26)}
.hero-title{position:absolute;left:369px;top:102px;font-size:33px;font-weight:300;color:var(--white)}
.hero-text{position:absolute;left:372px;top:146px;width:200px;font-size:10px;line-height:12px;color:var(--white)}
.hero-arrow{position:absolute;top:126px}

.section-title{position:absolute;left:0;width:691px;text-align:center;font-size:23px;font-weight:300;color:var(--ink)}

.project-card{position:absolute;top:391px;width:162px;height:168px;background:var(--white);border:1px solid var(--line)}
.project-photo{height:95px}
.project-title{margin:9px 9px 0;font-size:10.5px;font-weight:400}
.project-text{margin:5px 9px 0;font-size:6.6px;line-height:10.5px;color:var(--ink)}

.capabilities{position:absolute;left:0;top:578px;width:691px;height:356px;background:var(--band)}
.cap-panel{position:absolute;top:48px;width:282px;height:276px;background:var(--white)}
.cap-head{height:32px;background:var(--red);color:var(--white);font-size:13.5px;font-weight:400;padding:7px 17px;position:relative}
.cap-head svg{position:absolute;right:15px;top:11px}
.cap-list{list-style:none;padding:0 4px}
.cap-list li{height:25.6px;border-bottom:1px dotted #999;font-size:8.8px;color:var(--muted);display:flex;align-items:center;gap:8px;padding-left:10px;padding-top:3px}
.cap-list li:last-child{border-bottom:none}

.contact-form .field{position:absolute;left:130px;width:188px;height:25px;border:1px solid var(--line);font-size:9px;color:var(--muted);padding:6px 8px}
.contact-form .upload-field{display:flex;align-items:center;gap:6px;padding:4px 6px}
.upload-btn{background:var(--band);border:1px solid var(--line);padding:1px 6px;font-size:8px;color:var(--ink)}
.privacy-note{position:absolute;left:130px;top:1150px;width:188px;font-size:7px;color:var(--muted)}
.submit-btn{position:absolute;left:131px;top:1164px;width:75px;height:24px;background:var(--red);color:var(--white);font-size:12.5px;text-align:center;line-height:24px}
.contact-info{position:absolute;left:365px;font-size:10.5px;color:var(--ink)}
.contact-info span{display:inline-block;width:20px}
.social{position:absolute;top:1110px;width:29px;height:29px;border:1px solid var(--ink);border-radius:50%;display:flex;align-items:center;justify-content:center}
.copyright{position:absolute;left:365px;top:1173px;font-size:6.5px;color:var(--muted)}
</style>
</head>
<body>

<header class="site-header">
  <div class="brand"><span class="brand-dot"></span>Brightmoor</div>
  <nav class="main-nav">
    <a style="left:396px">Home</a>
    <a style="left:447px">About Us</a>
    <a style="left:512px">Services</a>
    <a style="left:574px">Contact Us</a>
  </nav>
</header>

<section class="hero" role="img" aria-label="Close-up of a glowing filament light bulb against warm blurred lights">
  <svg class="hero-arrow" style="left:55px" width="16" height="28" viewBox="0 0 16 28"><polyline points="14,1 2,14 14,27" fill="none" stroke="#fff" stroke-width="1.5"/></svg>
  <svg class="hero-arrow" style="left:614px" width="16" height="28" viewBox="0 0 16 28"><polyline points="2,1 14,14 2,27" fill="none" stroke="#fff" stroke-width="1.5"/></svg>
  <h1 class="hero-title">Lorium Ipsum</h1>
  <p class="hero-text">Excepteur sint occaecat cupidatat non proident, sunt in culpa qui officia deserunt mollit anim id est laborum</p>
</section>

<h2 class="section-title" style="top:345px">Completed projects</h2>

<article class="project-card" style="left:55px">
  <div class="project-photo" role="img" aria-label="Completed residential townhouses" style="background:linear-gradient(180deg,#7fb1e0 0,#c9d9e6 45%,#6d6a66 60%,#9a958d 100%)"></div>
  <h3 class="project-title">Aliquam erat ac ipsum</h3>
  <p class="project-text">Lorem ipsum dolor sit amet enim. Etiam ullamcorper. Suspendisse a pellentesque dui, non felis.</p>
</article>
<article class="project-card" style="left:265px">
  <div class="project-photo" role="img" aria-label="Completed commercial warehouse units" style="background:linear-gradient(180deg,#a9c6e2 0,#dfe7ee 25%,#55585c 40%,#7b7b78 70%,#8f8e8a 100%)"></div>
  <h3 class="project-title">Aliquam erat ac ipsum</h3>
  <p class="project-text">Lorem ipsum dolor sit amet enim. Etiam ullamcorper. Suspendisse a pellentesque dui, non felis.</p>
</article>
<article class="project-card" style="left:473px">
  <div class="project-photo" role="img" aria-label="Completed interior function room with lighting" style="background:linear-gradient(180deg,#c8c6c0 0,#e6e3dc 45%,#8a7b68 75%,#5f5243 100%)"></div>
  <h3 class="project-title">Aliquam erat ac ipsum</h3>
  <p class="project-text">Lorem ipsum dolor sit amet enim. Etiam ullamcorper. Suspendisse a pellentesque dui, non felis.</p>
</article>

<section class="capabilities">
  <h2 class="section-title" style="top:5px">Our capabilities</h2>

  <div class="cap-panel" style="left:55px">
    <div class="cap-head">Residential
      <svg width="16" height="9" viewBox="0 0 16 9"><polygon points="5,0 0,4.5 5,9" fill="#fff"/><polygon points="11,0 16,4.5 11,9" fill="#fff"/></svg>
    </div>
    <ul class="cap-list">
      <li><svg width="8" height="7" viewBox="0 0 8 7"><polyline points="1,3.5 3,5.5 7,1" fill="none" stroke="#e0232a" stroke-width="1.8"/></svg>24hr Support / faults</li>
      <li><svg width="8" height="7" viewBox="0 0 8 7"><polyline points="1,3.5 3,5.5 7,1" fill="none" stroke="#e0232a" stroke-width="1.8"/></svg>RCD (Safety Switch) installations</li>
      <li><svg width="8" height="7" viewBox="0 0 8 7"><polyline points="1,3.5 3,5.5 7,1" fill="none" stroke="#e0232a" stroke-width="1.8"/></svg>Smoke alarms</li>
      <li><svg width="8" height="7" viewBox="0 0 8 7"><polyline points="1,3.5 3,5.5 7,1" fill="none" stroke="#e0232a" stroke-width="1.8"/></svg>Power points</li>
      <li><svg width="8" height="7" viewBox="0 0 8 7"><polyline points="1,3.5 3,5.5 7,1" fill="none" stroke="#e0232a" stroke-width="1.8"/></svg>Lighting points</li>
      <li><svg width="8" height="7" viewBox="0 0 8 7"><polyline points="1,3.5 3,5.5 7,1" fill="none" stroke="#e0232a" stroke-width="1.8"/></svg>External lighting</li>
      <li><svg width="8" height="7" viewBox="0 0 8 7"><polyline points="1,3.5 3,5.5 7,1" fill="none" stroke="#e0232a" stroke-width="1.8"/></svg>Sensor lighting</li>
      <li><svg width="8" height="7" viewBox="0 0 8 7"><polyline points="1,3.5 3,5.5 7,1" fill="none" stroke="#e0232a" stroke-width="1.8"/></svg>Switching</li>
      <li><svg width="8" height="7" viewBox="0 0 8 7"><polyline points="1,3.5 3,5.5 7,1" fill="none" stroke="#e0232a" stroke-width="1.8"/></svg>Antennas and Arial points</li>
    </ul>
  </div>

  <div class="cap-panel" style="left:353px">
    <div class="cap-head">Commercial / Industrial
      <svg width="16" height="9" viewBox="0 0 16 9"><polygon points="5,0 0,4.5 5,9" fill="#fff"/><polygon points="11,0 16,4.5 11,9" fill="#fff"/></svg>
    </div>
    <ul class="cap-list">
      <li><svg width="8" height="7" viewBox="0 0 8 7"><polyline points="1,3.5 3,5.5 7,1" fill="none" stroke="#e0232a" stroke-width="1.8"/></svg>24hr Support / faults</li>
      <li><svg width="8" height="7" viewBox="0 0 8 7"><polyline points="1,3.5 3,5.5 7,1" fill="none" stroke="#e0232a" stroke-width="1.8"/></svg>Lighting/power design and consultation</li>
      <li><svg width="8" height="7" viewBox="0 0 8 7"><polyline points="1,3.5 3,5.5 7,1" fill="none" stroke="#e0232a" stroke-width="1.8"/></svg>Commercial lighting</li>
      <li><svg width="8" height="7" viewBox="0 0 8 7"><polyline points="1,3.5 3,5.5 7,1" fill="none" stroke="#e0232a" stroke-width="1.8"/></svg>Emergency and exit lighting</li>
      <li><svg width="8" height="7" viewBox="0 0 8 7"><polyline points="1,3.5 3,5.5 7,1" fill="none" stroke="#e0232a" stroke-width="1.8"/></svg>Led strip lighting</li>
      <li><svg width="8" height="7" viewBox="0 0 8 7"><polyline points="1,3.5 3,5.5 7,1" fill="none" stroke="#e0232a" stroke-width="1.8"/></svg>Energy efficient lighting</li>
      <li><svg width="8" height="7" viewBox="0 0 8 7"><polyline points="1,3.5 3,5.5 7,1" fill="none" stroke="#e0232a" stroke-width="1.8"/></svg>Temporary lighting</li>
      <li><svg width="8" height="7" viewBox="0 0 8 7"><polyline points="1,3.5 3,5.5 7,1" fill="none" stroke="#e0232a" stroke-width="1.8"/></svg>Illuminated signage</li>
      <li><svg width="8" height="7" viewBox="0 0 8 7"><polyline points="1,3.5 3,5.5 7,1" fill="none" stroke="#e0232a" stroke-width="1.8"/></svg>Switchboard relocations</li>
    </ul>
  </div>
</section>

<h2 class="section-title" style="top:942px">Contact Us</h2>

<div class="contact-form">
  <div class="field" style="top:990px">Name</div>
  <div class="field" style="top:1020px">Phone</div>
  <div class="field" style="top:1050px">Email Address</div>
  <div class="field" style="top:1080px;height:40px">Message</div>
  <div class="field upload-field" style="top:1124px;height:23px"><span class="upload-btn">Choose file</span>Attach plans</div>
  <p class="privacy-note">We do not disclose information to third parties.</p>
  <div class="submit-btn">Submit</div>
</div>

<p class="contact-info" style="top:998px"><span>P:</span> +48 12 345 678 901</p>
<p class="contact-info" style="top:1024px"><span>E:</span> hello@brightmoor-electric.com</p>
<p class="contact-info" style="top:1050px"><span>W:</span> www.brightmoor-electric.com</p>
<p class="contact-info" style="top:1075px"><span>A:</span> Poland, Cracow, Lipowa 7</p>

<a class="social" style="left:361px" aria-label="Social profile link">
  <svg width="13" height="13" viewBox="0 0 13 13"><circle cx="3" cy="6.5" r="1.8" fill="#333"/><circle cx="10" cy="2.5" r="1.8" fill="#333"/><circle cx="10" cy="10.5" r="1.8" fill="#333"/><line x1="3" y1="6.5" x2="10" y2="2.5" stroke="#333"/><line x1="3" y1="6.5" x2="10" y2="10.5" stroke="#333"/></svg>
</a>
<a class="social" style="left:403px" aria-label="Message link">
  <svg width="13" height="12" viewBox="0 0 13 12"><path d="M1 1h11v7H5l-3 3V8H1z" fill="none" stroke="#333" stroke-width="1.2" stroke-linejoin="round"/></svg>
</a>
<a class="social" style="left:445px" aria-label="Email link">
  <svg width="13" height="10" viewBox="0 0 13 10"><rect x=".6" y=".6" width="11.8" height="8.8" fill="none" stroke="#333" stroke-width="1.2"/><polyline points="1,1 6.5,5.5 12,1" fill="none" stroke="#333" stroke-width="1.2"/></svg>
</a>

<p class="copyright">© 2015 www.brightmoor-electric.com. All rights reserved.</p>

</body>
</html>
```